Maple Crest Branding for Contracts and Customer facing documents

We are hoping to create a themed branding for our company. We would like to leverage this across our contracts, documents, and all client information and proposals. www.HomesByMapleCrest.example is our website. We are selling high end custom homes. We am intending to use this template for a Lead Magnet and other marketing.

Target Market(s)

Luxury Custom Home Buyers

Industry/Entity Type

Residential Construction

Other font styles liked:
• You may choose, We want to be elegant but very legible and professional

Colors
0054AA
0677BA
7BADD7
CADEEF
E8F1F8

```html
<!DOCTYPE html>
<html lang="en">
<head>
<meta charset="utf-8">
<title>Maple Crest – Customer Design Agreement Package</title>
<link rel="stylesheet" href="https://fonts.googleapis.com/css2?family=Playfair+Display:ital,wght@0,400;1,400&family=Montserrat:wght@500&display=swap">
<style>
  :root {
    --backdrop: #a4a6ae;
    --navy: #17293a;
    --white: #ffffff;
    --gold: #d9a24a;
    --body-text: #e6e4df;
    --photo-sky: #8fa3c4;
    --photo-dusk: #c9b7c8;
    --photo-house: #8c96a6;
    --photo-ground: #4f4a44;
  }
  * { box-sizing: border-box; margin: 0; padding: 0; }
  html, body { width: 1200px; height: 849px; overflow: hidden; }
  body {
    background: radial-gradient(ellipse at 50% 45%, #b1b3ba 0%, var(--backdrop) 70%);
    font-family: "Playfair Display", Georgia, serif;
    position: relative;
  }
  .page {
    position: absolute;
    top: 80px;
    width: 485px;
    height: 688px;
    background: var(--white);
    overflow: hidden;
    box-shadow: 0 2px 8px rgba(0,0,0,0.25);
  }
  .page--cover { left: 92px; }
  .page--agreement { left: 623px; }
  .page-shapes { position: absolute; inset: 0; width: 485px; height: 688px; }

  .brand { position: absolute; display: flex; align-items: center; gap: 10px; color: var(--navy); }
  .brand-mark { width: 12px; height: 12px; background: var(--navy); flex: none; }
  .brand-name { font-weight: 400; line-height: 1; white-space: nowrap; }
  .brand-tag { font-family: "Montserrat", Arial, sans-serif; letter-spacing: 2px; font-weight: 500; }
  .brand-url { font-family: "Montserrat", Arial, sans-serif; font-weight: 500; }

  .cover-brand { left: 40px; top: 34px; display: block; }
  .cover-brand .brand-row { display: flex; align-items: center; gap: 10px; }
  .cover-brand .brand-name { font-size: 32px; }
  .cover-brand .brand-tag { font-size: 8.5px; margin: 6px 0 0 54px; }
  .cover-brand .brand-url { font-size: 6px; margin: 3px 0 0 60px; letter-spacing: 0.5px; }

  .cover-title {
    position: absolute; left: 45px; top: 522px;
    color: var(--gold); font-size: 34px; line-height: 39px; font-weight: 400;
  }
  .cover-subtitle {
    position: absolute; left: 45px; top: 614px;
    color: var(--gold); font-size: 24px; letter-spacing: 0.5px; font-weight: 400;
  }
  .cover-year {
    position: absolute; right: 24px; top: 596px;
    color: var(--white); font-size: 44px; line-height: 1; font-weight: 400;
  }
  .site-footer {
    position: absolute; font-family: "Montserrat", Arial, sans-serif;
    font-size: 6px; letter-spacing: 1px; color: var(--white); font-weight: 500; white-space: nowrap;
  }
  .cover-footer { right: 24px; top: 648px; }

  .agreement-brand { left: 20px; top: 16px; display: block; }
  .agreement-brand .brand-row { display: flex; align-items: center; gap: 6px; }
  .agreement-brand .brand-mark { width: 7px; height: 7px; }
  .agreement-brand .brand-name { font-size: 16px; }
  .agreement-brand .brand-tag { font-size: 5px; margin: 3px 0 0 30px; letter-spacing: 1px; }
  .agreement-brand .brand-url { font-size: 3.5px; margin: 2px 0 0 32px; }

  .doc-title {
    position: absolute; left: 143px; width: 300px; top: 26px;
    text-align: center; color: var(--navy); font-size: 21px; font-weight: 400; letter-spacing: 0.3px;
  }
  .doc-tier {
    position: absolute; left: 143px; width: 300px; top: 56px;
    text-align: center; color: var(--gold); font-size: 20px; font-weight: 400;
  }

  .doc-text {
    position: absolute; left: 70px; width: 338px;
    color: var(--body-text); font-size: 10.6px; line-height: 16.5px;
    text-align: justify; text-align-last: justify;
  }
  .doc-intro { top: 184px; text-align-last: left; }
  .doc-intro::before {
    content: ""; position: absolute; left: -15px; top: 3px; width: 3px; height: 88px; background: var(--gold);
  }
  .doc-heading {
    position: absolute; left: 52px; color: var(--gold);
    font-size: 18px; font-weight: 400; letter-spacing: 0.2px;
  }
  .heading-recitals { top: 288px; }
  .heading-terms { top: 436px; left: 55px; }
  .doc-recitals { top: 322px; }
  .part-bar {
    position: absolute; left: 67px; top: 473px; width: 352px; height: 17px;
    background: var(--gold); color: var(--navy);
    font-style: italic; font-size: 12px; line-height: 17px; padding-left: 3px;
  }
  .part-bar .part-label { margin-right: 18px; }
  .doc-services { top: 508px; height: 116px; overflow: hidden; }
  .agreement-footer { left: 70px; top: 656px; }
</style>
</head>
<body>

<section class="page page--cover">
  <svg class="page-shapes" viewBox="0 0 485 688" aria-hidden="true">
    <polygon points="0,154 485,91 485,688 0,688" fill="var(--navy)"/>
  </svg>
  <svg class="page-shapes" viewBox="0 0 485 688" role="img" aria-label="Photo of a two-storey grey-sided custom home with a brick base and covered balcony at dusk">
    <defs>
      <linearGradient id="photoTone" x1="0" y1="0" x2="0.3" y2="1">
        <stop offset="0" stop-color="var(--photo-sky)"/>
        <stop offset="0.25" stop-color="var(--photo-dusk)"/>
        <stop offset="0.45" stop-color="var(--photo-house)"/>
        <stop offset="1" stop-color="var(--photo-ground)"/>
      </linearGradient>
    </defs>
    <polygon points="0,154 485,91 485,550 0,418" fill="url(#photoTone)"/>
  </svg>

  <div class="brand cover-brand">
    <div class="brand-row"><span class="brand-mark"></span><span class="brand-name">Maple Crest</span></div>
    <div class="brand-tag">CUSTOM HOMES</div>
    <div class="brand-url">www.HomesByMapleCrest.example</div>
  </div>

  <h1 class="cover-title">Customer<br>Design Agreement</h1>
  <p class="cover-subtitle">PACKAGE</p>
  <p class="cover-year">2025</p>
  <p class="site-footer cover-footer">HOMESBYMAPLECREST.EXAMPLE</p>
</section>

<section class="page page--agreement">
  <svg class="page-shapes" viewBox="0 0 485 688" aria-hidden="true">
    <polygon points="0,163 485,91 485,688 0,688" fill="var(--navy)"/>
  </svg>

  <div class="brand agreement-brand">
    <div class="brand-row"><span class="brand-mark"></span><span class="brand-name">Maple Crest</span></div>
    <div class="brand-tag">CUSTOM HOMES</div>
    <div class="brand-url">www.HomesByMapleCrest.example</div>
  </div>

  <h2 class="doc-title">SERVICES AGREEMENT</h2>
  <p class="doc-tier">Bronze</p>

  <p class="doc-text doc-intro">This services agreement (this “Agreement”), is effective as of the date when executed by the last party to sign on the final page of this Agreement (the “Effective Date”) and is by and between Client Company , a Client State Incorporation Description (“Client”) and Harbor Ledger Contract Services, LLC, an Oregon limited liability company (“Agent”).</p>

  <h3 class="doc-heading heading-recitals">RECITALS</h3>
  <p class="doc-text doc-recitals">Whereas Client and Agent desire to enter into an arrangement whereby Agent provides Client with basic bookkeeping, payroll, and financial reporting services upon the terms set forth in this Agreement. Now, therefore, in consideration of the mutual promises and agreements set forth herein, and other good and valuable consideration, the parties hereto agree as follows:</p>

  <h3 class="doc-heading heading-terms">AGREEMENT TERMS</h3>
  <p class="part-bar"><span class="part-label">PART 1</span>Services Provided</p>
  <p class="doc-text doc-services">Cloud-Based Archive and Storage of Client Information: Agent will exercise commercially reasonable care to organize and safeguard the privacy of any client invoices, receipts, bills, financial documents or general legal documents stored by Agent or Client in the cloud storage system provided by Agent to Client which is based on technology provided by CloudVault.example® or a similar system. All Client documents will be sorted and filed by Agent, and Client will have access to all Client documentation via a login and password issued by Agent for the duration of this Agreement.</p>

  <p class="site-footer agreement-footer">HOMESBYMAPLECREST.EXAMPLE</p>
</section>

</body>
</html>
```